The Harbor Circle (By Line: Shaping Tomorrow with Steady Guidance)

I am seeking the design and creation of a”banner ad image” for my radio program entitled “The Harbor Circle.” The banner created should capture the look and feel of an image that reflects the vision statement below and that fosters the intent reflected by the principal goals listed below:

Vision statement

The Harbor Circle is a powerfully engaging platform for great conversations about leadership and leadership learning.

Goals

1. Build a community of listeners who will be made to feel invited and excited about being connected to the show, it host and its broader community of listeners.

2. Provide interesting, intelligent and meaningful conversations about leadership and learning by the host, invited guests, both in studio and online.
The banner should be one that speaks to/invites listeners to become members of a community of listeners seeking to listen to and learn about the subject of leadership and leadership improvement.

The acceptable (final) banner should be professional in image, style and substance. The Photo shop layered file is required so that the banner image can be altered and adapted for use in PDF or text documents.

Finally, it is a banner that I intend to repopulate across several medium’s, such as netvyne, pal page, etc. as a part of the process of establishing an image – brand – for the radio show as reflected the vision statement and goals.

While the target audience described is broad, it is anticipated that the primary listeners will be those who are leaders and serving in such roles as CEO’s, Vice Presidents, and other leaders in business, government and other local organizational capacities including students interested in learning about and discussing the subject of leadership.

Target Market(s)

Those who are interested in the topic of leadership and are actively engaged in leading as supervisors, managers and executives. These would be CEO, VP, and other C-level leaders in business, private and public sector organizations. It is also anticipated that those who are students of leadership learning will find my program a great resource.

Industry/Entity Type

Radio

Colors
3176b5
b768aa
d3a5cc

Requirements
Must have
• Be unique, attractive and capture the look and feel as noted in the description of the project.
Nice to have
• Note: I will have a head shot photo included in the banner so a place holder needs to be included for that

```html
<!DOCTYPE html>
<html lang="en">
<head>
<meta charset="utf-8">
<title>The Harbor Circle – Banner</title>
<link rel="stylesheet" href="https://fonts.googleapis.com/css2?family=Roboto:ital,wght@0,700;1,700&display=swap">
<style>
  :root {
    --bg-deep: #040406;
    --bg-glow: #34343f;
    --title: #c9202b;
    --tagline: #ffffff;
    --piece-dark: #08080a;
    --piece-light: #2c2c33;
  }
  html, body {
    margin: 0;
    padding: 0;
    width: 1200px;
    height: 600px;
    overflow: hidden;
    background: var(--bg-deep);
  }
  .banner {
    position: relative;
    width: 1200px;
    height: 600px;
    overflow: hidden;
    background:
      radial-gradient(ellipse 520px 420px at 200px 250px, var(--bg-glow) 0%, rgba(20,20,26,0.6) 45%, transparent 80%),
      linear-gradient(180deg, #0d0d12 0%, var(--bg-deep) 100%);
  }
  .hero-art {
    position: absolute;
    left: 120px;
    top: 40px;
    width: 196px;
    height: 560px;
    border-radius: 40px 40px 8px 8px;
    background: linear-gradient(90deg, var(--piece-dark) 0%, var(--piece-light) 35%, var(--piece-dark) 100%);
  }
  .title {
    position: absolute;
    left: 372px;
    top: 108px;
    margin: 0;
    font-family: "Roboto", sans-serif;
    font-weight: 700;
    font-size: 108px;
    line-height: 1.02;
    letter-spacing: -1px;
    color: var(--title);
  }
  .title-line {
    display: block;
    white-space: nowrap;
  }
  .tagline {
    position: absolute;
    left: 374px;
    top: 496px;
    margin: 0;
    font-family: "Roboto", sans-serif;
    font-style: italic;
    font-weight: 700;
    font-size: 22.5px;
    line-height: 1.45;
    color: var(--tagline);
  }
</style>
</head>
<body>
  <main class="banner">
    <div class="hero-art" role="img" aria-label="Glossy black chess king wearing a red necktie, reflected on a dark surface"></div>
    <h1 class="title">
      <span class="title-line">The</span>
      <span class="title-line">Harbor</span>
      <span class="title-line">Circle</span>
    </h1>
    <p class="tagline">Powerfully engaging platform for great conversations<br>about leadership and leadership learning.</p>
  </main>
</body>
</html>
```